Fenwick and Torrance Postcard Design

Greetings!
Lawyers hire me as an expert witness. They take a gamble on hiring me in hopes of winning their case.
This postcard will be printed in jumbo size through Quillmark. The design must meet these specifications:

Full Bleed Size (starting document size)
11.12" x 6.12"
282 x 155 mm
3335 x 1835 pixels
* Finished artwork should use the full bleed dimensions for best results.
Document Trim Size (final size after being cut)
11.00" x 6.00"
279 x 152 mm
3300 x 1800 pixels
* Please be sure to keep all text and photos within the safe cutting margin.
Resolution
300 DPI
Visit Quillmark for more details or to download a design template:
https://www.quillmark-example.com/product-presentation-info.aspx?productPresentationId=1590#
https://www.quillmark-example.com/vp/ns/propath/UploadResources.aspx?selectedTab=0?pfid=BDW&pf_id=BDW&xnav=product-page#FileFormats

1. The postcard will have a Blank Backside.
2. I like a black, white and red color theme with a serious legalistic font.
3. In regards to color theme, see https://www.cardorbit-example.com/designs/security-system-postcards/#security-system-postcards-4
4. 8 preferred background images in alphabetical order from favorite to least favorite, but all are great:
a. https://files.driftbox-example.com/f/s!QwErTy12ZxCvBn34MnBvCx56LkJhGf
5. Header Text:
a. (line 1) Dr. K.R. Torrance, Psy.D., NCEB
b. (lines 2 and 3) Psychological Evaluator, Board-Certified Forensic Psychologist and National Expert Witness
c. (Line 4 in bold and more prominent than text in lines 1-3) 4 Signs of a Proficient & Credible Psyc. Expert
6. View this checklist image for inspiration, https://lnk.tidepoint-example.com/images/8RqWm3 and use the following text within such a checklist image:
7. Board Certified by the Continental Council of Courtroom Behavioral Science (CCCB)?
Yes, I'm Board Certified. This mark of proficiency in forensic psychology is recognized by judicial decisions, statutes and regulations.
8. Fellow of the Cont. Fellowship of Legal Behavioral Study?
Yes, I'm a CFLB Fellow, along with some of the field's most prominent leaders comprising the academic arm of the CCCB.
9. A Recognized Leader Amongst Other Experts?
I’m the 2018 duly elected President of the Hudson Valley Behavioral Guild Section on Courtroom Assessment, and a Board Member of the Coalition of Practitioners for Youth Safeguarding.
10. Positioned in Roles of Trust and Neutrality by Judges?
Yes, I work as an in-house Harborview Juvenile Tribunal mental-health expert in proceedings regarding competency, imminent risk, sentencing, custody, child maltreatment and TPR.
11. The following should be prominent along the bottom:
12. BOOK A LUNCH & LEARN AT YOUR OFFICE
Visit http://offer.witnessbench-example.com Call 555-014-2937
Designer: This call to action (CTA) for #12 needs to pop off of the page. It needs to draw the reader's eye. It needs depth, like the way a CTA button looks like on a website. Play around w/ idea to accomplish this (e.g., adding badges, icons, shapes, a picture, an image of someone presenting it, etc).
13. List my areas of specialization somewhere
• CPS & Matrimonial Issues
• Competency
• Juvenile Delinquency
• Criminal Sentencing
• Personal Injury and Civil Rights
• Immigration
• Fitness for Duty, SSD and Workers Comp
• Sex-Offenders
• IME and Neuropsychological Testing
• Behind-The-Scenes Consulting on A Contingency Fee
• Low-Price Initial Screening Evaluations
• Therapy Services & Programs for Litigants
14. Put this test somewhere and keep it subtle: I recognize the importance of your work. You can trust my assistance.
15. Put this in fine print somewhere (can be 2 lines): Fenwick and Torrance, LLC. 2018 New York Licensed Psychologist Lic. # 047213 - New Jersey Licensed Psychologist Lic. # 72K900315847

Target Market(s)

Lawyers

Industry/Entity Type

Hire

Font styles to use
Serif

Colors
ec1f27
ffffff

Requirements
Must have
• An awesome call to action. If the CTA doesn't catch the eye, then it won't work. The point of this postcard is to get them to that website so I can capture their email address. Anything else is a secondary gain. Consider 3-d design elements to give it pop and depth.
Should not have
• There's a big difference between a red rectangle and a red button on a website that has that 3d quality. This postcard has a lot of words. It can easily become just a bunch of text on a colorful piece of paper w/ a pic. Avoid this by segmenting the space, layering Diff color text on Diff color background and incorporating 3d design elements and shapes.

```html
<!DOCTYPE html>
<html lang="en">
<head>
<meta charset="utf-8">
<title>Fenwick and Torrance Postcard</title>
<link rel="stylesheet" href="https://fonts.googleapis.com/css2?family=Bebas+Neue&family=Oswald:wght@300;400&family=Signika:wght@400;600&family=Roboto+Slab:wght@700&family=Oxygen:wght@300;400&display=swap">
<style>
  :root {
    --red: #ec1f27;
    --red-deep: #b5121a;
    --red-dark: #8e0c12;
    --black: #111111;
    --ink: #1a1a1a;
    --white: #ffffff;
    --stage: #adadad;
    --paper: #eeeeee;
  }
  * { box-sizing: border-box; margin: 0; padding: 0; }
  html, body { width: 1105px; height: 1200px; overflow: hidden; }
  body { background: var(--stage); position: relative; font-family: "Signika", sans-serif; }

  .side-label {
    position: absolute; left: 0; width: 1105px; text-align: center;
    font-family: "Oxygen", sans-serif; font-weight: 400; font-size: 28px;
    color: var(--ink); letter-spacing: 1px;
  }
  .side-label.front { top: 44px; }
  .side-label.back { top: 1122px; }

  .card {
    position: absolute; overflow: hidden;
    box-shadow: 0 14px 18px -8px rgba(0,0,0,.45);
  }
  .card-front { left: 126px; top: 96px; width: 868px; height: 478px; background: var(--white); }
  .card-back { left: 124px; top: 618px; width: 870px; height: 478px; background: var(--paper); }

  /* header */
  .header {
    position: absolute; left: 0; top: 0; width: 868px; height: 102px;
    background: linear-gradient(180deg, #fafafa 0%, #e4e4e4 100%);
  }
  .name {
    position: absolute; left: 20px; top: 14px;
    font-family: "Bebas Neue", sans-serif; font-size: 50px; line-height: 1;
    color: var(--ink); letter-spacing: 0.5px; white-space: nowrap;
  }
  .name .accent { color: var(--red); }
  .credentials-line {
    position: absolute; left: 21px; top: 66px;
    font-family: "Oswald", sans-serif; font-weight: 300; font-size: 14.5px;
    color: var(--ink); white-space: nowrap;
  }
  .header-divider {
    position: absolute; left: 558px; top: 22px; width: 1px; height: 62px; background: #b9b9b9;
  }
  .signs-title {
    position: absolute; left: 573px; top: 20px;
    font-family: "Bebas Neue", sans-serif; font-size: 36px; line-height: 33px;
    color: var(--ink); white-space: nowrap;
  }
  .signs-title .num { color: var(--red); }

  /* middle band */
  .feature-band { position: absolute; left: 0; top: 102px; width: 868px; height: 287px; }
  .feature-band svg.band-shapes { position: absolute; inset: 0; }

  .specialty-pill {
    position: absolute; left: 326px; top: 16px; width: 204px; height: 27px;
    border-radius: 14px;
    background: linear-gradient(180deg, #ffffff 0%, #d9d9d9 100%);
    box-shadow: 0 3px 5px rgba(0,0,0,.4);
    font-family: "Bebas Neue", sans-serif; font-size: 17px; line-height: 28px;
    color: var(--red); text-align: center; letter-spacing: .3px;
  }
  .specialty-list {
    position: absolute; left: 330px; top: 55px; list-style: none;
    color: var(--white); font-size: 10.6px; font-weight: 400;
  }
  .specialty-list li { position: relative; padding-left: 15px; line-height: 13px; margin-bottom: 3.8px; }
  .specialty-list li svg { position: absolute; left: 0; top: 2px; width: 10px; height: 10px; }

  .list-divider {
    position: absolute; left: 558px; top: 8px; width: 1px; height: 270px;
    background: rgba(0,0,0,.22); box-shadow: 1px 0 0 rgba(255,255,255,.12);
  }

  .sign { position: absolute; left: 574px; width: 285px; color: var(--white); }
  .sign svg { position: absolute; left: 0; top: -1px; width: 18px; height: 18px; }
  .sign h3 { margin-left: 24px; font-size: 10.6px; font-weight: 600; line-height: 12px; }
  .sign p { margin-left: 24px; margin-top: 4px; font-size: 7.8px; line-height: 11.6px; font-weight: 400; }
  .sign-1 { top: 16px; }
  .sign-2 { top: 86px; }
  .sign-3 { top: 145px; }
  .sign-4 { top: 216px; }

  /* action bar */
  .action-bar {
    position: absolute; left: 0; top: 389px; width: 868px; height: 89px;
    background: linear-gradient(180deg, #262626 0%, #0c0c0c 100%);
  }
  .action-divider { position: absolute; left: 298px; top: 10px; width: 1px; height: 70px; background: #3a3a3a; }
  .cta-button {
    position: absolute; left: 28px; top: 19px; width: 250px; height: 55px;
    border-radius: 28px;
    background: linear-gradient(180deg, #f5424a 0%, var(--red) 45%, var(--red-dark) 100%);
    border: 2px solid #ff6b70;
    box-shadow: 0 6px 10px rgba(0,0,0,.7), inset 0 -3px 4px rgba(0,0,0,.3), inset 0 2px 2px rgba(255,255,255,.3);
    color: var(--white);
  }
  .cta-main {
    position: absolute; left: 24px; top: 8px;
    font-family: "Roboto Slab", serif; font-weight: 700; font-size: 21px; line-height: 1;
    text-shadow: 0 2px 2px rgba(0,0,0,.45);
  }
  .cta-sub {
    position: absolute; left: 25px; top: 33px;
    font-family: "Oxygen", sans-serif; font-size: 10px; letter-spacing: .3px;
  }
  .cta-arrow {
    position: absolute; right: 8px; top: 8px; width: 36px; height: 36px; border-radius: 50%;
    background: radial-gradient(circle at 40% 35%, #3a3a3a, #0a0a0a);
    box-shadow: 0 2px 3px rgba(0,0,0,.6);
  }
  .cta-arrow svg { position: absolute; left: 9px; top: 9px; width: 18px; height: 18px; }

  .contact-line {
    position: absolute; left: 314px; top: 11px; white-space: nowrap;
    font-family: "Bebas Neue", sans-serif; color: var(--white); line-height: 30px; height: 30px;
  }
  .contact-line .icon { display: inline-block; vertical-align: middle; width: 24px; height: 24px; margin-right: 5px; position: relative; top: -3px; }
  .contact-line .url { font-size: 24px; }
  .contact-line .sep { font-size: 26px; margin: 0 10px; }
  .contact-line .phone { font-size: 29px; }
  .tagline {
    position: absolute; left: 316px; top: 44px;
    font-family: "Oxygen", sans-serif; font-weight: 300; font-size: 16.5px; color: var(--white); white-space: nowrap;
  }
  .fine-print {
    position: absolute; left: 317px; top: 70px;
    font-family: "Oxygen", sans-serif; font-size: 7.9px; color: #e6e6e6; white-space: nowrap;
  }

  /* back */
  .back-top { position: absolute; left: 0; top: 0; width: 870px; height: 30px; background: linear-gradient(180deg, var(--red) 0%, var(--red-deep) 100%); }
  .back-image {
    position: absolute; left: 0; top: 30px; width: 870px; height: 410px;
    background: radial-gradient(ellipse at 85% 80%, #d2d2d2 0%, #e4e4e4 45%, #f0f0f0 75%);
  }
  .back-rule { position: absolute; left: 0; top: 440px; width: 870px; height: 6px; background: var(--white); }
  .back-bottom { position: absolute; left: 0; top: 446px; width: 870px; height: 32px; background: linear-gradient(180deg, #222 0%, #080808 100%); }
</style>
</head>
<body>

<div class="side-label front">FRONT</div>

<section class="card card-front">
  <header class="header">
    <h1 class="name"><span class="accent">Dr. K.R. Torrance,</span> Psy.D., NCEB</h1>
    <p class="credentials-line">Psychological Evaluator, Board-Certified Forensic Psychologist &amp; National Expert Witness</p>
    <div class="header-divider"></div>
    <h2 class="signs-title"><span class="num">4</span> Signs of a Proficient<br>&amp; Credible Psyc. Expert</h2>
  </header>

  <div class="feature-band">
    <svg class="band-shapes" width="868" height="287" viewBox="0 0 868 287">
      <defs>
        <linearGradient id="redField" x1="0" y1="0" x2="0" y2="1">
          <stop offset="0" stop-color="#d8161e"/>
          <stop offset="1" stop-color="#a80f16"/>
        </linearGradient>
        <linearGradient id="photoTone" x1="0" y1="0" x2="1" y2="1">
          <stop offset="0" stop-color="#4a4440"/>
          <stop offset="0.5" stop-color="#7a6652"/>
          <stop offset="1" stop-color="#c9b79a"/>
        </linearGradient>
      </defs>
      <rect width="868" height="287" fill="url(#redField)"/>
      <path d="M0,0 H300 C346,80 350,200 300,287 H0 Z" fill="#111"/>
      <path d="M0,0 H284 C330,80 334,200 286,287 H0 Z" fill="#f2f2f2"/>
      <path d="M0,0 H278 C322,80 326,200 278,287 H0 Z" fill="url(#photoTone)" role="img" aria-label="Photo of a Lady Justice statue holding balance scales in front of blurred law books"/>
    </svg>

    <div class="specialty-pill">List My Areas of Specialization</div>
    <ul class="specialty-list">
      <li><svg viewBox="0 0 10 10"><circle cx="5" cy="5" r="4.2" fill="none" stroke="#fff" stroke-width="1"/><path d="M3 5.1 L4.5 6.5 L7.2 3.6" fill="none" stroke="#fff" stroke-width="1.2"/></svg>CPS &amp; Matrimonial Issues</li>
      <li><svg viewBox="0 0 10 10"><circle cx="5" cy="5" r="4.2" fill="none" stroke="#fff" stroke-width="1"/><path d="M3 5.1 L4.5 6.5 L7.2 3.6" fill="none" stroke="#fff" stroke-width="1.2"/></svg>Competency</li>
      <li><svg viewBox="0 0 10 10"><circle cx="5" cy="5" r="4.2" fill="none" stroke="#fff" stroke-width="1"/><path d="M3 5.1 L4.5 6.5 L7.2 3.6" fill="none" stroke="#fff" stroke-width="1.2"/></svg>Juvenile Delinquency</li>
      <li><svg viewBox="0 0 10 10"><circle cx="5" cy="5" r="4.2" fill="none" stroke="#fff" stroke-width="1"/><path d="M3 5.1 L4.5 6.5 L7.2 3.6" fill="none" stroke="#fff" stroke-width="1.2"/></svg>Criminal Sentencing</li>
      <li><svg viewBox="0 0 10 10"><circle cx="5" cy="5" r="4.2" fill="none" stroke="#fff" stroke-width="1"/><path d="M3 5.1 L4.5 6.5 L7.2 3.6" fill="none" stroke="#fff" stroke-width="1.2"/></svg>Personal Injury and Civil Rights</li>
      <li><svg viewBox="0 0 10 10"><circle cx="5" cy="5" r="4.2" fill="none" stroke="#fff" stroke-width="1"/><path d="M3 5.1 L4.5 6.5 L7.2 3.6" fill="none" stroke="#fff" stroke-width="1.2"/></svg>Immigration</li>
      <li><svg viewBox="0 0 10 10"><circle cx="5" cy="5" r="4.2" fill="none" stroke="#fff" stroke-width="1"/><path d="M3 5.1 L4.5 6.5 L7.2 3.6" fill="none" stroke="#fff" stroke-width="1.2"/></svg>Fitness for Duty, SSD and Workers Comp</li>
      <li><svg viewBox="0 0 10 10"><circle cx="5" cy="5" r="4.2" fill="none" stroke="#fff" stroke-width="1"/><path d="M3 5.1 L4.5 6.5 L7.2 3.6" fill="none" stroke="#fff" stroke-width="1.2"/></svg>Sex-Offenders</li>
      <li><svg viewBox="0 0 10 10"><circle cx="5" cy="5" r="4.2" fill="none" stroke="#fff" stroke-width="1"/><path d="M3 5.1 L4.5 6.5 L7.2 3.6" fill="none" stroke="#fff" stroke-width="1.2"/></svg>IME and Neuropsychological Testing</li>
      <li><svg viewBox="0 0 10 10"><circle cx="5" cy="5" r="4.2" fill="none" stroke="#fff" stroke-width="1"/><path d="M3 5.1 L4.5 6.5 L7.2 3.6" fill="none" stroke="#fff" stroke-width="1.2"/></svg>Behind-The-Scenes Consulting on<br>A Contingency Fee</li>
      <li><svg viewBox="0 0 10 10"><circle cx="5" cy="5" r="4.2" fill="none" stroke="#fff" stroke-width="1"/><path d="M3 5.1 L4.5 6.5 L7.2 3.6" fill="none" stroke="#fff" stroke-width="1.2"/></svg>Low-Price Initial Screening Evaluations</li>
      <li><svg viewBox="0 0 10 10"><circle cx="5" cy="5" r="4.2" fill="none" stroke="#fff" stroke-width="1"/><path d="M3 5.1 L4.5 6.5 L7.2 3.6" fill="none" stroke="#fff" stroke-width="1.2"/></svg>Therapy Services and Programs for Litigants</li>
    </ul>

    <div class="list-divider"></div>

    <article class="sign sign-1">
      <svg viewBox="0 0 18 18"><circle cx="9" cy="9" r="7.8" fill="none" stroke="#fff" stroke-width="1.6"/><path d="M5 9.2 L8 12 L14.5 4.8" fill="none" stroke="#fff" stroke-width="2"/></svg>
      <h3>Board Certified by the Continental Council of Courtroom Behavioral Science (CCCB)?</h3>
      <p>Yes, I'm Board Certified. This mark of proficiency in forensic psychology is recognized by judicial decisions, statutes and regulations.</p>
    </article>
    <article class="sign sign-2">
      <svg viewBox="0 0 18 18"><circle cx="9" cy="9" r="7.8" fill="none" stroke="#fff" stroke-width="1.6"/><path d="M5 9.2 L8 12 L14.5 4.8" fill="none" stroke="#fff" stroke-width="2"/></svg>
      <h3>Fellow of the Cont. Fellowship of Legal Behavioral Study?</h3>
      <p>Yes, I'm a CFLB Fellow, along with some of the field's most prominent leaders, comprising the academic arm of the CCCB.</p>
    </article>
    <article class="sign sign-3">
      <svg viewBox="0 0 18 18"><circle cx="9" cy="9" r="7.8" fill="none" stroke="#fff" stroke-width="1.6"/><path d="M5 9.2 L8 12 L14.5 4.8" fill="none" stroke="#fff" stroke-width="2"/></svg>
      <h3>A Recognized Leader Amongst Other Experts?</h3>
      <p>I'm the 2018 duly elected President of the Hudson Valley Behavioral Guild Section on Courtroom Assessment, and a Board Member of the Coalition of Practitioners for Youth Safeguarding.</p>
    </article>
    <article class="sign sign-4">
      <svg viewBox="0 0 18 18"><circle cx="9" cy="9" r="7.8" fill="none" stroke="#fff" stroke-width="1.6"/><path d="M5 9.2 L8 12 L14.5 4.8" fill="none" stroke="#fff" stroke-width="2"/></svg>
      <h3>Positioned in Roles of Trust and Neutrality by Judges?</h3>
      <p>Yes, I'm an in-house Harborview Juvenile Tribunal mental-health expert for proceedings regarding competency, imminent risk, sentencing, custody, child maltreatment and TPR.</p>
    </article>
  </div>

  <footer class="action-bar">
    <div class="cta-button">
      <span class="cta-main">BOOK A LUNCH</span>
      <span class="cta-sub">&amp; LEARN AT YOUR OFFICE</span>
      <span class="cta-arrow"><svg viewBox="0 0 18 18"><path d="M2 9 H14 M9 3.5 L14.5 9 L9 14.5" fill="none" stroke="#fff" stroke-width="2.6" stroke-linecap="round" stroke-linejoin="round"/></svg></span>
    </div>
    <div class="action-divider"></div>
    <div class="contact-line">
      <svg class="icon" viewBox="0 0 24 24"><circle cx="12" cy="12" r="11" fill="var(--red)"/><circle cx="12" cy="12" r="7" fill="none" stroke="#7a0a0f" stroke-width="1.2"/><path d="M5 12 H19 M12 5 C8 9 8 15 12 19 C16 15 16 9 12 5" fill="none" stroke="#7a0a0f" stroke-width="1.1"/></svg><span class="url">http://offer.witnessbench-example.com</span><span class="sep">|</span><svg class="icon" viewBox="0 0 24 24"><circle cx="12" cy="12" r="11" fill="var(--red)"/><path d="M8.2 6 L10.2 8.8 L9 10.4 C9.8 12.2 11.4 13.9 13.4 14.9 L15 13.7 L17.8 15.6 L16.6 17.8 C12 17.6 6.6 12.4 6.2 7.4 Z" fill="#111"/></svg><span class="phone">555-014-2937</span>
    </div>
    <p class="tagline">I recognize the importance of your work. You can trust my assistance.</p>
    <p class="fine-print">Fenwick and Torrance, LLC. 2018 New York Licensed Psychologist Lic. # 047213 - New Jersey Licensed Psychologist Lic. # 72K900315847</p>
  </footer>
</section>

<section class="card card-back">
  <div class="back-top"></div>
  <div class="back-image" role="img" aria-label="Faint pale photo of a classical courthouse colonnade with curved cornice"></div>
  <div class="back-rule"></div>
  <div class="back-bottom"></div>
</section>

<div class="side-label back">BACK</div>

</body>
</html>
```